Modern Corvane Tree Care Website

I need a website for a full service Tree Care company. The company provides tree pruning, tree removal, tree preservation, emergency services, stump grinding, and emergency tree services.

Target Market(s)

Customers that need tree services

Industry/Entity Type

Landscaping, Tree Services

Coding

Coded - Design and coding required

Number of Pages Required

5+ page

Font styles to use
Sans Serif

Requirements
Must have
• Good clean design that showcases the services the company provides.
Nice to have
• Services page; contact form, blog, home page, about page

```html
<!DOCTYPE html>
<html lang="en">
<head>
<meta charset="utf-8">
<title>Corvane Tree Care</title>
<link href="https://fonts.googleapis.com/css2?family=Inter:wght@400;500;600;700;800&display=swap" rel="stylesheet">
<style>
:root{
  --green:#8cc63f;
  --green-dark:#3d6b1a;
  --green-deep:#2f5512;
  --tint:#f5fbec;
  --ink:#1b1b1b;
  --body:#444;
  --nav:#2a2a2a;
  --panel:#1f1f1f;
  --white:#fff;
}
*{box-sizing:border-box;margin:0;padding:0}
html,body{width:1200px;height:4488px;overflow:hidden}
body{font-family:"Inter",Helvetica,Arial,sans-serif;color:var(--ink);background:var(--white);position:relative}
.abs{position:absolute}
section,header,nav,footer{position:absolute;left:0;width:1200px}
.brand{display:flex;align-items:center;gap:10px;font-weight:800;font-size:22px;color:var(--ink);letter-spacing:.3px;white-space:nowrap}
.brand .mark{width:40px;height:40px;background:var(--green);flex:none}
.btn{position:absolute;display:flex;align-items:center;justify-content:center;gap:10px;background:var(--green);color:var(--white);font-size:12px;font-weight:600;text-decoration:none}
.btn svg{width:16px;height:10px}
.eyebrow{color:var(--green);font-size:13px;letter-spacing:.3px;text-transform:uppercase}
.h2{font-size:35px;font-weight:700;color:var(--ink)}
.center{text-align:center;width:1200px;left:0}

/* header */
.topbar{top:0;height:111px}
.topbar .brand{position:absolute;left:139px;top:35px}
.contact-item{position:absolute;top:30px;display:flex;gap:12px;align-items:center}
.contact-item .ring{width:50px;height:50px;border:2px solid var(--green);border-radius:50%;display:flex;align-items:center;justify-content:center}
.contact-item b{display:block;font-size:12px;font-weight:600}
.contact-item span{font-size:11px;color:var(--body)}
.mainnav{top:111px;height:70px;background:var(--nav)}
.mainnav ul{list-style:none;display:flex;gap:36px;position:absolute;left:139px;top:26px;font-size:13px;font-weight:600;color:var(--white)}
.mainnav li.active{color:var(--green)}
.mainnav .btn{left:895px;top:0;width:162px;height:70px;font-size:13px}

/* hero */
.hero{top:181px;height:500px;background:linear-gradient(100deg,#2f5a16 0%,#4a7d22 45%,#6f9a3a 100%)}
.hero .kicker{left:139px;top:132px;color:var(--white);font-size:24px}
.hero h1{position:absolute;left:139px;top:180px;color:var(--white);font-size:44px;font-weight:800;line-height:61px;letter-spacing:.5px}
.hero .btn{left:141px;top:315px;width:188px;height:51px}

/* services */
.services{top:681px;height:852px}
.services .eyebrow{top:86px}
.services .h2{top:117px}
.svc{position:absolute;width:293px;height:272px;text-align:center;padding-top:34px}
.svc.tint{background:var(--tint)}
.svc .ic{width:78px;height:78px;border-radius:50%;background:var(--green);margin:0 auto;display:flex;align-items:center;justify-content:center}
.svc h3{font-size:17px;font-weight:600;margin-top:18px}
.svc p{font-size:11px;line-height:19px;color:var(--body);margin:10px auto 0;width:225px}
.svc a{display:inline-block;margin-top:12px;font-size:13px;font-weight:600;color:var(--green);text-decoration:underline}
.svc.feature{background:var(--green);color:var(--white);padding-top:66px}
.svc.feature h3{color:var(--white)}
.svc.feature p{color:var(--white)}
.svc.feature .pill{display:inline-block;margin-top:12px;background:var(--white);color:var(--green);font-size:12px;font-weight:600;padding:9px 22px}

/* about */
.about{top:1533px;height:624px;background:var(--tint)}
.about .faint{left:66px;top:59px;width:56px;height:52px;background:var(--green);opacity:.18}
.about .eyebrow{left:141px;top:120px}
.about h2{position:absolute;left:141px;top:153px;font-size:32px;line-height:41px;font-weight:700}
.rule{position:absolute;left:0;height:2px;background:var(--green)}
.rule::after{content:"";position:absolute;right:-1px;top:-7px;width:2px;height:16px;background:var(--green)}
.about p{position:absolute;left:141px;top:279px;width:420px;font-size:12.5px;line-height:22.6px;color:var(--ink)}
.about .btn{left:141px;top:454px;width:155px;height:49px}
.about .photo{left:646px;top:92px;width:411px;height:442px;background:linear-gradient(160deg,#c8652a 0%,#7c4b2e 45%,#5a3a22 70%,#2e2a24 100%)}

/* cta */
.cta{top:2157px;height:367px;background:linear-gradient(90deg,#4f7f22,#5e8e2a 50%,#4a7a1f)}
.cta h2{position:absolute;top:94px;font-size:32px;font-weight:700;color:var(--white)}
.cta p{position:absolute;top:152px;left:230px;width:740px;text-align:center;font-size:12px;line-height:23px;color:var(--white)}
.cta .btn{left:507px;top:219px;width:186px;height:49px}

/* blog */
.blog{top:2524px;height:878px}
.blog .eyebrow{top:90px}
.blog .h2{top:124px}
.post{position:absolute;top:206px;width:294px;height:494px;background:var(--white);box-shadow:0 2px 10px rgba(0,0,0,.12)}
.post .img{position:relative;height:292px}
.post .date{position:absolute;left:2px;bottom:0;width:73px;height:99px;background:var(--green);color:var(--white);text-align:center;font-size:18px;font-weight:600;line-height:24px;padding-top:24px}
.post h3{font-size:17px;font-weight:600;margin:22px 0 0 22px}
.post p{font-size:11.5px;line-height:21px;color:var(--body);margin:12px 22px 0}
.post a{display:block;margin:9px 0 0 22px;font-size:13px;font-weight:600;color:var(--green);text-decoration:underline}
.blog .btn{left:510px;top:742px;width:166px;height:49px}

/* contact */
.contact{top:3402px;height:686px}
.contact .eyebrow{left:141px;top:56px}
.contact h2{position:absolute;left:141px;top:90px;font-size:33px;line-height:40px;font-weight:700}
.contact .intro{position:absolute;left:141px;top:210px;width:420px;font-size:12.5px;line-height:22.6px}
.feat{position:absolute;width:220px;display:flex;gap:12px}
.feat .fi{width:46px;height:46px;flex:none}
.feat b{display:block;color:var(--green);font-size:15px;font-weight:600}
.feat span{display:block;font-size:10.5px;line-height:17px;color:var(--body);margin-top:4px}
.estimate{left:622px;top:0;width:435px;height:596px;background:var(--panel)}
.estimate h3{position:absolute;left:40px;top:53px;color:var(--white);font-size:17px;font-weight:600}
.estimate h3::after{content:"";position:absolute;left:0;top:30px;width:70px;height:2px;background:var(--green)}
.field{position:absolute;left:43px;width:354px;background:var(--green);color:var(--white);font-size:13px;padding:18px 28px}
.estimate .submit{position:absolute;left:43px;top:493px;width:154px;height:47px;background:var(--white);color:var(--green);font-size:12px;font-weight:600;display:flex;align-items:center;justify-content:center;gap:8px}

/* footer */
.site-footer{top:4088px;height:326px;background:linear-gradient(100deg,#4d7d1f,#6b9a2e 55%,#5b8a25)}
.site-footer .brand{position:absolute;left:139px;top:143px;color:var(--white)}
.site-footer .brand .mark{background:var(--white)}
.fcol{position:absolute;top:92px;color:var(--white)}
.fcol h4{font-size:17px;font-weight:700;letter-spacing:.3px}
.fcol ul{list-style:none;margin-top:20px}
.fcol li{font-size:12px;line-height:24.4px}
.detail{display:flex;gap:10px;font-size:12px;line-height:18px;margin-bottom:12px}
.social li{display:flex;align-items:center;gap:12px;margin-bottom:11px;line-height:24px}
.social .dot{width:24px;height:24px;border:2px solid var(--white);border-radius:50%}
.copyright{top:4414px;height:74px;display:flex;align-items:center;justify-content:center;font-size:13px;font-weight:600}
</style>
</head>
<body>

<header class="topbar">
  <div class="brand"><span class="mark"></span>Corvane Tree Care</div>
  <div class="contact-item" style="left:449px">
    <div class="ring"><svg width="22" height="22" viewBox="0 0 24 24" fill="none" stroke="#8cc63f" stroke-width="1.6"><path d="M5 3h4l2 5-3 2a12 12 0 0 0 6 6l2-3 5 2v4a2 2 0 0 1-2 2A17 17 0 0 1 3 5a2 2 0 0 1 2-2z"/></svg></div>
    <div><b>Call</b><span>(555)014-2739</span></div>
  </div>
  <div class="contact-item" style="left:627px">
    <div class="ring"><svg width="22" height="22" viewBox="0 0 24 24" fill="none" stroke="#8cc63f" stroke-width="1.6"><rect x="3" y="6" width="18" height="13"/><path d="M3 6l9 7 9-7"/></svg></div>
    <div><b>Email</b><span>info@corvanetreecare.com</span></div>
  </div>
  <div class="contact-item" style="left:836px">
    <div class="ring"><svg width="22" height="22" viewBox="0 0 24 24" fill="none" stroke="#8cc63f" stroke-width="1.6"><path d="M12 22s7-7 7-12a7 7 0 0 0-14 0c0 5 7 12 7 12z"/><circle cx="12" cy="10" r="2.5"/></svg></div>
    <div><b>Location</b><span>Lorem Ipsum is simply dummy text.</span></div>
  </div>
</header>

<nav class="mainnav">
  <ul>
    <li class="active">[&nbsp; Home &nbsp;]</li><li>Services</li><li>About Us</li><li>Blog</li><li>Contact</li>
  </ul>
  <a class="btn" href="#">Get A Quote <svg viewBox="0 0 16 10" fill="none" stroke="#fff" stroke-width="1.6"><path d="M1 5h13M10 1l4 4-4 4"/></svg></a>
</nav>

<section class="hero" role="img" aria-label="Smiling gardener in an apron trimming topiary shrubs with hedge shears in a green garden">
  <div class="abs kicker">LET'S START YOUR</div>
  <h1>LANDSCAPING TREE<br>SERVICES</h1>
  <a class="btn" href="#">Contact Now <svg viewBox="0 0 16 10" fill="none" stroke="#fff" stroke-width="1.6"><path d="M1 5h13M10 1l4 4-4 4"/></svg></a>
</section>

<section class="services">
  <div class="abs center eyebrow">Our Services</div>
  <div class="abs center h2">Landscaping Tree Services</div>

  <div class="svc" style="left:139px;top:204px">
    <div class="ic"><svg width="40" height="40" viewBox="0 0 40 40" fill="none" stroke="#fff" stroke-width="2"><path d="M20 36V18M20 18c-6-2-9-8-8-13 6 1 9 6 8 13zM20 24c5-1 9-5 9-11-6 1-9 5-9 11z"/></svg></div>
    <h3>Tree Pruning</h3>
    <p>Lorem ipsum dolor sit amet, eiusmod tempor incididunt ut labore et dolore magna aliqua.</p>
    <a href="#">Read More</a>
  </div>
  <div class="svc tint" style="left:453px;top:204px">
    <div class="ic"><svg width="40" height="40" viewBox="0 0 40 40" fill="none" stroke="#fff" stroke-width="2"><circle cx="20" cy="15" r="10"/><path d="M20 25v12M14 37h12"/></svg></div>
    <h3>Tree Removal</h3>
    <p>Lorem ipsum dolor sit amet, eiusmod tempor incididunt ut labore et dolore magna aliqua.</p>
    <a href="#">Read More</a>
  </div>
  <div class="svc" style="left:765px;top:204px">
    <div class="ic"><svg width="40" height="40" viewBox="0 0 40 40" fill="none" stroke="#fff" stroke-width="2"><path d="M6 30h10l8-3 8-5M6 34h16l12-8M22 20c0-6 4-10 10-10 0 6-4 10-10 10z"/></svg></div>
    <h3>Tree Preservation</h3>
    <p>Lorem ipsum dolor sit amet, eiusmod tempor incididunt ut labore et dolore magna aliqua.</p>
    <a href="#">Read More</a>
  </div>
  <div class="svc tint" style="left:139px;top:498px">
    <div class="ic"><svg width="40" height="40" viewBox="0 0 40 40" fill="none" stroke="#fff" stroke-width="2"><circle cx="20" cy="20" r="13"/><path d="M20 12v8l5 4"/></svg></div>
    <h3>Emergency Services</h3>
    <p>Lorem ipsum dolor sit amet, eiusmod tempor incididunt ut labore et dolore magna aliqua.</p>
    <a href="#">Read More</a>
  </div>
  <div class="svc" style="left:453px;top:498px">
    <div class="ic"><svg width="40" height="40" viewBox="0 0 40 40" fill="none" stroke="#fff" stroke-width="2"><rect x="8" y="24" width="24" height="9"/><path d="M14 24c0-5 2-10 6-12 4 2 6 7 6 12"/></svg></div>
    <h3>Stump Grinding</h3>
    <p>Lorem ipsum dolor sit amet, eiusmod tempor incididunt ut labore et dolore magna aliqua.</p>
    <a href="#">Read More</a>
  </div>
  <div class="svc feature" style="left:765px;top:498px">
    <h3>CorvaneTreeCare</h3>
    <p>Lorem ipsum dolor sit amet, eiusmod tempor incididunt ut labore et dolore magna aliqua.</p>
    <span class="pill">View All Service</span>
  </div>
</section>

<section class="about">
  <div class="abs faint"></div>
  <div class="abs eyebrow">About Us</div>
  <h2>CorvaneTreeCare Landscaping<br>Tree Services</h2>
  <div class="rule" style="top:256px;width:204px"></div>
  <p>Lorem ipsum dolor sit amet, consectetur adipiscing elit, sed do eiusmod tempor incididunt ut labore et dolore magna aliqua. Quis ipsum suspendisse ultrices gravida. Risus commodo viverra maecenas accumsan lacus vel facilisis Lorem ipsum dolor sit amet, consectetur adipiscing elit, sed do eiusmod tempor incididunt ut labore et dolore magna aliqua. Quis ipsum suspendisse ultrices gravida. Risus commodo viverra maecenas accumsan lacus vel facilisis.</p>
  <a class="btn" href="#">Read More <svg viewBox="0 0 16 10" fill="none" stroke="#fff" stroke-width="1.6"><path d="M1 5h13M10 1l4 4-4 4"/></svg></a>
  <div class="abs photo" role="img" aria-label="Arborist in ear protection guiding a large log through an orange sawmill"></div>
</section>

<section class="cta" role="img" aria-label="Parent and child watering and planting young trees in a sunny garden, tinted green">
  <h2 class="center" style="text-align:center">Transform Your Landscape With CorvaneTreeCare!</h2>
  <p>Enhance the beauty and health of your outdoor space with our expert tree services. Whether you need tree trimming, removal, or emergency care, our skilled team is here to help.</p>
  <a class="btn" href="#">(555) 013-9939 <svg viewBox="0 0 16 10" fill="none" stroke="#fff" stroke-width="1.6"><path d="M1 5h13M10 1l4 4-4 4"/></svg></a>
</section>

<section class="blog">
  <div class="abs center eyebrow">Our Blog</div>
  <div class="abs center h2">Landscaping Tree Services</div>

  <article class="post" style="left:139px">
    <div class="img" role="img" aria-label="Man lifting a heavy log section outdoors" style="background:linear-gradient(160deg,#6f8f4a,#4f6a33 60%,#3d4b2a)"><div class="date">09<br>MAY</div></div>
    <h3>Lorem ipsum dolor sit</h3>
    <p>Lorem ipsum dolor sit amet, consectetur adipiscing elit, sed do eiusmod tempor incididunt ut labore et dolore magna aliqua. Quis ipsum suspendisse ultrices</p>
    <a href="#">Read More</a>
  </article>
  <article class="post" style="left:453px">
    <div class="img" role="img" aria-label="Worker with a chainsaw in a sunlit forest" style="background:linear-gradient(180deg,#b9b3a2,#8e8270 55%,#6a5d4c)"><div class="date">09<br>MAY</div></div>
    <h3>Lorem ipsum dolor sit</h3>
    <p>Lorem ipsum dolor sit amet, consectetur adipiscing elit, sed do eiusmod tempor incididunt ut labore et dolore magna aliqua. Quis ipsum suspendisse ultrices</p>
    <a href="#">Read More</a>
  </article>
  <article class="post" style="left:765px">
    <div class="img" role="img" aria-label="Hand splitting firewood with a red axe on a pile of logs" style="background:linear-gradient(160deg,#6b5a48,#8a7560 50%,#4a3e32)"><div class="date">09<br>MAY</div></div>
    <h3>Lorem ipsum dolor sit</h3>
    <p>Lorem ipsum dolor sit amet, consectetur adipiscing elit, sed do eiusmod tempor incididunt ut labore et dolore magna aliqua. Quis ipsum suspendisse ultrices</p>
    <a href="#">Read More</a>
  </article>

  <a class="btn" href="#">View All Blogs <svg viewBox="0 0 16 10" fill="none" stroke="#fff" stroke-width="1.6"><path d="M1 5h13M10 1l4 4-4 4"/></svg></a>
</section>

<section class="contact">
  <div class="abs eyebrow">Contact Form</div>
  <h2>Why Most of The People<br>Choose Us</h2>
  <div class="rule" style="top:189px;width:204px"></div>
  <p class="intro">Lorem ipsum dolor sit amet, consectetur adipiscing elit, sed do eiusmod tempor incididunt ut labore et dolore magna aliqua. Quis ipsum suspendisse ultrices gravida. Risus commodo viverra maecenas accumsan lacus vel facilisis.</p>

  <div class="feat" style="left:139px;top:361px">
    <svg class="fi" viewBox="0 0 46 46" fill="none" stroke="#8cc63f" stroke-width="2"><path d="M6 24a17 17 0 0 1 34 0"/><rect x="3" y="22" width="7" height="12"/><rect x="36" y="22" width="7" height="12"/><text x="13" y="32" font-size="11" fill="#8cc63f" stroke="none" font-family="Inter,sans-serif">24</text></svg>
    <div><b>Available 24/7</b><span>Lorem ipsum dolor sit amet, consectetur adipiscing elit, sed do eiusmod tempor</span></div>
  </div>
  <div class="feat" style="left:380px;top:361px">
    <svg class="fi" viewBox="0 0 46 46" fill="none" stroke="#8cc63f" stroke-width="2"><path d="M4 20L40 6 30 40 20 26zM20 26L40 6"/></svg>
    <div><b>Free quotation</b><span>Lorem ipsum dolor sit amet, consectetur adipiscing elit, sed do eiusmod tempor</span></div>
  </div>
  <div class="feat" style="left:139px;top:469px">
    <svg class="fi" viewBox="0 0 46 46" fill="none" stroke="#8cc63f" stroke-width="2"><path d="M23 8a10 10 0 0 0-6 18v5h12v-5A10 10 0 0 0 23 8zM18 36h10"/></svg>
    <div><b>Creative ideas</b><span>Lorem ipsum dolor sit amet, consectetur adipiscing elit, sed do eiusmod tempor</span></div>
  </div>
  <div class="feat" style="left:380px;top:469px">
    <svg class="fi" viewBox="0 0 46 46" fill="none" stroke="#8cc63f" stroke-width="2"><circle cx="23" cy="16" r="7"/><path d="M10 40a13 13 0 0 1 26 0"/></svg>
    <div><b>Customer Focused</b><span>Lorem ipsum dolor sit amet, consectetur adipiscing elit, sed do eiusmod tempor</span></div>
  </div>

  <form class="abs estimate">
    <h3>Free Estimate</h3>
    <div class="field" style="top:122px;height:56px">Name</div>
    <div class="field" style="top:200px;height:56px">Email</div>
    <div class="field" style="top:279px;height:55px">Phone No</div>
    <div class="field" style="top:357px;height:112px">Your Message Here</div>
    <div class="submit">Submit Now <svg width="16" height="10" viewBox="0 0 16 10" fill="none" stroke="#8cc63f" stroke-width="1.6"><path d="M1 5h13M10 1l4 4-4 4"/></svg></div>
  </form>
</section>

<footer class="site-footer" role="img" aria-label="Arborist climbing a tree, tinted green">
  <div class="brand"><span class="mark"></span>Corvane Tree Care</div>
  <div class="fcol" style="left:456px">
    <h4>QUICK LINKS</h4>
    <ul><li>Home</li><li>About Us</li><li>Services</li><li>Blog</li><li>Contact</li></ul>
  </div>
  <div class="fcol" style="left:669px">
    <h4>CONTACT DETAILS</h4>
    <div style="margin-top:20px">
      <div class="detail"><svg width="12" height="16" viewBox="0 0 12 16" fill="#fff"><path d="M6 16S0 9 0 6a6 6 0 0 1 12 0c0 3-6 10-6 10z"/></svg>Lorem ipsum dolor sit amet.</div>
      <div class="detail"><svg width="12" height="14" viewBox="0 0 24 24" fill="#fff"><path d="M5 3h4l2 5-3 2a12 12 0 0 0 6 6l2-3 5 2v4a2 2 0 0 1-2 2A17 17 0 0 1 3 5a2 2 0 0 1 2-2z"/></svg><span>Phone<br>(555)014-2739</span></div>
      <div class="detail"><svg width="13" height="12" viewBox="0 0 24 20" fill="#fff"><path d="M0 2h24v16H0z"/></svg><span>Email<br>info@corvanetreecare.com</span></div>
    </div>
  </div>
  <div class="fcol" style="left:956px">
    <h4>FOLLOW US</h4>
    <ul class="social">
      <li><span class="dot"></span>Friendline</li>
      <li><span class="dot"></span>Chirper</li>
      <li><span class="dot"></span>Vidstream</li>
      <li><span class="dot"></span>Snapgram</li>
    </ul>
  </div>
</footer>

<div class="abs copyright" style="left:0;width:1200px">Copyright © 2024 CorvaneTreeCare Landscaping Tree Services.</div>

</body>
</html>
```